使い方
①角形2号(縦)
ご入居のお問合せをもらったお客様へパンフレットを送付するときに使用

②長形3号(縦)
お客様、業者宛てに資料を送付するときに使用

③窓付長形3号(横)
入居中のお客様へ請求書を送付するときに使用

記載項目
①、②、③の封筒に記載する情報
会社ロゴマーク
会社名:株式会社ミモザ・ケアリンク
□すまいる鷹野 〒007-0931 北海道札幌市東区栄町五条2丁目7-3 ミモザ・ブライト第2 TEL:011-734-2918 FAX:011-746-8153
□すまいる鷹野西 〒063-0942 北海道札幌市西区山手三条9丁目6-11
TEL:011-652-3184 FAX:011-652-3196

①、②の封筒に記載する情報
郵便番号の枠
希望イメージ
シンプル 複雑
単色 カラフル
暗い 明るい
日常 高級
遊び心 厳粛
未来的 伝統的
女性的 男性的
希望する色
黄・オレンジ系
納品ファイル
• 高解像度JPG (.jpg)
• イラストレーター形式 (.ai)
補足説明
■ 選んだ理由

弊社が運営している施設のあたたかさを感じられる作品を選ばせていただきました。ロゴマークをそのままスタンプにするのではなく、ロゴデザインを封筒に映えるデザインとしてうまく落とし込んでいただけたことがよかったです。

■ 提案者全員のお礼・コメント

この度は、封筒デザインについてご提案いただきまして誠にありがとうございました。どれも素晴らしいデザインでありました。

```html
<!DOCTYPE html>
<html lang="ja">
<head>
<meta charset="utf-8">
<title>角形2号封筒 ミモザ・ケアリンク</title>
<link rel="stylesheet" href="https://fonts.googleapis.com/css2?family=M+PLUS+Rounded+1c:wght@500;700&family=Noto+Sans+JP:wght@400;500;700&display=swap">
<style>
  :root {
    --paper: #ffffff;
    --ground: #f2f2f2;
    --edge: #bdbdbd;
    --orange: #f4a020;
    --yellow: #f7c531;
    --pale: #fdf0d6;
    --ink: #3a3a3a;
    --muted: #8a8a8a;
  }
  * { margin: 0; padding: 0; box-sizing: border-box; }
  html, body { width: 851px; height: 1200px; overflow: hidden; background: var(--ground); }
  body { font-family: "Noto Sans JP", sans-serif; color: var(--ink); position: relative; }

  .spec-note { position: absolute; left: 14px; top: 10px; font-size: 9px; color: var(--muted); letter-spacing: .03em; }

  .envelope { position: absolute; left: 20px; top: 44px; width: 811px; height: 1140px; background: var(--paper); border: 1px solid var(--edge); }
  .flap-line { position: absolute; left: 0; right: 0; top: 150px; border-top: 1px dashed var(--edge); }

  .flap-mark { position: absolute; top: 62px; left: 50%; transform: translateX(-50%); display: flex; align-items: center; gap: 8px; }
  .flap-mark .name { font-family: "M PLUS Rounded 1c", sans-serif; font-weight: 700; font-size: 22px; color: var(--orange); }
  .flap-mark .dot { width: 14px; height: 14px; border-radius: 50%; background: var(--yellow); }

  .postal-boxes { position: absolute; top: 248px; left: 470px; display: flex; gap: 6px; }
  .postal-boxes span { width: 30px; height: 38px; border: 2px solid var(--orange); }
  .postal-boxes .hyphen-gap { width: 8px; border: none; }

  .sender-mark { position: absolute; left: 108px; top: 690px; height: 230px; border-left: 8px solid var(--yellow); padding-left: 18px; }
  .sender-mark .symbol { width: 46px; height: 46px; border-radius: 50%; background: var(--orange); margin: 14px 0 20px; }
  .sender-mark .name { font-family: "M PLUS Rounded 1c", sans-serif; font-weight: 700; font-size: 46px; color: var(--orange); line-height: 1; }
  .sender-mark .company { font-size: 17px; font-weight: 700; margin-top: 22px; color: var(--ink); }
  .sender-mark .url { font-size: 10px; color: var(--muted); margin-top: 8px; }

  .bg-accent { position: absolute; left: 470px; top: 670px; width: 280px; height: 280px; }

  .offices { position: absolute; left: 105px; right: 60px; top: 990px; display: flex; gap: 40px; }
  .office { flex: 1; }
  .office h2 { font-size: 19px; font-weight: 500; padding-bottom: 6px; border-bottom: 2px solid var(--orange); display: flex; align-items: center; gap: 8px; }
  .office h2 .box { width: 15px; height: 15px; border: 1.5px solid var(--ink); display: inline-block; }
  .office p { font-size: 10.5px; line-height: 1.55; margin-top: 6px; }
  .office .tel { display: flex; gap: 14px; align-items: center; margin-top: 2px; }
  .office .tel b { font-size: 15px; font-weight: 500; letter-spacing: .02em; }
  .office .tel small { font-size: 10px; }
  .office .date { font-size: 9px; color: var(--muted); margin-top: 10px; letter-spacing: .6em; text-align: center; }
</style>
</head>
<body>
  <div class="spec-note">角2封筒 240×332mm　フタの部分（ベロ40mm）ベロ部分のロゴ（仮押印）</div>

  <div class="envelope">
    <div class="flap-mark"><span class="name">すまいる</span><span class="dot"></span></div>
    <div class="flap-line"></div>

    <div class="postal-boxes">
      <span></span><span></span><span></span>
      <span class="hyphen-gap"></span>
      <span></span><span></span><span></span><span></span>
    </div>

    <svg class="bg-accent" viewBox="0 0 280 280" aria-hidden="true">
      <circle cx="140" cy="140" r="140" fill="var(--pale)"/>
    </svg>

    <div class="sender-mark">
      <div class="symbol"></div>
      <div class="name">すまいる</div>
      <div class="company">株式会社ミモザ・ケアリンク</div>
      <div class="url">http://www.mimoza-carelink.co.jp</div>
    </div>

    <div class="offices">
      <section class="office">
        <h2><span class="box"></span>すまいる鷹野</h2>
        <p>〒007-0931<br>北海道札幌市東区栄町五条2丁目7-3 ミモザ・ブライト第2</p>
        <div class="tel"><b>TEL 011-734-2918</b><small>FAX 011-746-8153</small></div>
        <div class="date">担当 年 月 日</div>
      </section>
      <section class="office">
        <h2><span class="box"></span>すまいる鷹野西</h2>
        <p>〒063-0942<br>北海道札幌市西区山手三条9丁目6-11</p>
        <div class="tel"><b>TEL 011-652-3184</b><small>FAX 011-652-3196</small></div>
        <div class="date">担当 年 月 日</div>
      </section>
    </div>
  </div>
</body>
</html>
```